Brookfen 14 Industrial Park Needs Website

We are looking for a website for a new project we are working on.
Project does not have a logo so just use text. Needs to be responsive and mobile friendly for all browsers and coded for both Android & IOS. SEO is also important. Want something visually grabbing that displays growth, quality and confidence.
WordPress or Joomla – must be desktop and mobile friendly with fast page load speed. Need the ability to edit ourselves.
See attached website brief for further information.
Industry/Entity Type
Land Sale/Lease/Development
Coding
Coded - Design and coding required
Number of Pages Required
4 page
Look and feel
Each slider illustrates characteristics of the customer's brand and the style your logo design should communicate.

```html
<!DOCTYPE html>
<html lang="en">
<head>
<meta charset="UTF-8">
<title>Brookfen 14 Industrial Park</title>
<link href="https://fonts.googleapis.com/css2?family=Poppins:wght@400;500;600;700&display=swap" rel="stylesheet">
<style>
  :root {
    --brand-blue: #0054a6;
    --icon-blue: #1a6ec4;
    --accent-blue: #0b6bc2;
    --map-grey: #ebebeb;
    --map-water: #cfe3f3;
    --marker-navy: #2e3192;
    --marker-edge: #161650;
    --pin-pink: #ee3d8f;
    --pin-orange: #f39a1e;
    --pin-blue: #0b5ea8;
    --text-dark: #333333;
    --text-body: #454545;
    --white: #ffffff;
  }
  * { box-sizing: border-box; margin: 0; padding: 0; }
  html, body { width: 1200px; height: 675px; overflow: hidden; }
  body { font-family: "Poppins", sans-serif; background: var(--white); }

  .page { position: relative; width: 1200px; height: 675px; overflow: hidden; }

  .region-map {
    position: absolute; left: 113px; top: 0; width: 1087px; height: 675px;
    background: radial-gradient(ellipse at 45% 55%, #eef0f1 0%, var(--map-grey) 55%, #e3ebf1 100%);
  }

  .town-marker { position: absolute; left: 509px; top: 305px; width: 131px; height: 85px; }
  .town-marker__label {
    position: absolute; left: 0; top: 0; width: 131px; height: 56px;
    background: var(--marker-navy); border: 2px solid var(--marker-edge);
    color: var(--white); font-weight: 700; font-size: 23px;
    display: flex; align-items: center; justify-content: center; letter-spacing: .3px;
  }
  .town-marker svg { position: absolute; left: 45px; top: 54px; }
  .town-name {
    position: absolute; left: 535px; top: 394px; font-size: 15px;
    color: #6a6a6a; font-weight: 500;
  }

  .pin { position: absolute; }

  .sidebar {
    position: absolute; left: 0; top: 0; width: 113px; height: 675px;
    background: var(--brand-blue);
  }
  .nav-home {
    position: absolute; left: 0; top: 185px; width: 226px; height: 44px;
    background: var(--brand-blue); display: flex; align-items: center;
  }
  .nav-home svg { margin-left: 45px; }
  .nav-home span { margin-left: 53px; color: var(--white); font-size: 14px; }
  .nav-icon {
    position: absolute; left: 38px; width: 39px; height: 39px; border-radius: 50%;
    background: var(--icon-blue); display: flex; align-items: center; justify-content: center;
  }

  .info-panel {
    position: absolute; left: 821px; top: 92px; width: 379px; height: 492px;
    background: rgba(255,255,255,.95); padding: 26px 0 0 43px;
  }
  .info-panel__title {
    font-size: 27px; line-height: 31px; font-weight: 600; color: var(--text-dark);
  }
  .info-panel__text {
    margin-top: 12px; width: 300px; font-size: 12.3px; line-height: 20.6px; color: var(--text-body);
  }
  .stats { display: flex; margin-top: 18px; }
  .stat { text-align: center; }
  .stat:nth-child(1) { width: 78px; }
  .stat:nth-child(2) { width: 90px; margin-left: 33px; }
  .stat:nth-child(3) { width: 60px; margin-left: 18px; }
  .stat__value { font-size: 25px; font-weight: 600; color: var(--accent-blue); line-height: 30px; }
  .stat__label { font-size: 11.2px; line-height: 16px; color: var(--text-body); margin-top: 4px; }
  .btn-learn {
    display: flex; align-items: center; justify-content: center;
    margin-top: 26px; width: 124px; height: 44px; background: var(--brand-blue);
    color: var(--white); font-weight: 600; font-size: 11.5px; letter-spacing: .2px;
  }
</style>
</head>
<body>
<div class="page">
  <div class="region-map" role="img" aria-label="Road map of the region around Wrenford with lakes, rivers and highways"></div>

  <svg class="pin" style="left:228px;top:246px" width="36" height="48" viewBox="0 0 36 48">
    <ellipse cx="18" cy="44" rx="11" ry="3" fill="#bdbdbd"/>
    <path d="M18 2C9 2 2 9 2 18c0 10 16 26 16 26s16-16 16-26C34 9 27 2 18 2z" fill="var(--pin-pink)"/>
    <circle cx="18" cy="17" r="5" fill="#fff"/>
  </svg>
  <svg class="pin" style="left:782px;top:550px" width="36" height="48" viewBox="0 0 36 48">
    <ellipse cx="18" cy="44" rx="11" ry="3" fill="#bdbdbd"/>
    <path d="M18 2C9 2 2 9 2 18c0 10 16 26 16 26s16-16 16-26C34 9 27 2 18 2z" fill="var(--pin-pink)"/>
    <circle cx="18" cy="17" r="5" fill="#fff"/>
  </svg>
  <svg class="pin" style="left:1096px;top:52px" width="36" height="44" viewBox="0 0 36 44">
    <path d="M18 2C9 2 2 9 2 18c0 10 16 24 16 24s16-14 16-24C34 9 27 2 18 2z" fill="var(--pin-orange)"/>
    <circle cx="18" cy="17" r="5" fill="#fff"/>
  </svg>
  <svg class="pin" style="left:1066px;top:-14px" width="40" height="48" viewBox="0 0 40 48">
    <path d="M20 2C10 2 2 10 2 20c0 11 18 26 18 26s18-15 18-26C38 10 30 2 20 2z" fill="var(--pin-blue)"/>
  </svg>

  <div class="town-marker">
    <div class="town-marker__label">WRENFORD</div>
    <svg width="42" height="32" viewBox="0 0 42 32">
      <path d="M10 0h22v10h9L21 31 1 10h9z" fill="var(--marker-navy)" stroke="var(--marker-edge)" stroke-width="2"/>
    </svg>
  </div>
  <div class="town-name">Wrenford</div>

  <nav class="sidebar">
    <a class="nav-home">
      <svg width="24" height="22" viewBox="0 0 24 22"><path d="M12 1L1 11h3v10h6v-6h4v6h6V11h3z" fill="#fff"/></svg>
      <span>HOME</span>
    </a>
    <a class="nav-icon" style="top:274px">
      <svg width="16" height="22" viewBox="0 0 16 22"><path d="M2 6a6 6 0 1 1 9 5c-2 1-3 2-3 4" fill="none" stroke="#fff" stroke-width="3.2" stroke-linecap="round"/><circle cx="8" cy="20" r="2" fill="#fff"/></svg>
    </a>
    <a class="nav-icon" style="top:363px">
      <svg width="18" height="18" viewBox="0 0 18 18" fill="#fff"><rect x="0" y="0" width="8" height="10"/><rect x="10" y="0" width="8" height="6"/><rect x="0" y="12" width="8" height="6"/><rect x="10" y="8" width="8" height="10"/></svg>
    </a>
    <a class="nav-icon" style="top:447px">
      <svg width="22" height="22" viewBox="0 0 24 24"><path d="M6.6 10.8a15 15 0 0 0 6.6 6.6l2.2-2.2c.3-.3.7-.4 1-.2 1.1.4 2.3.6 3.6.6.6 0 1 .4 1 1V20c0 .6-.4 1-1 1A17 17 0 0 1 3 4c0-.6.4-1 1-1h3.5c.6 0 1 .4 1 1 0 1.3.2 2.5.6 3.6.1.3 0 .7-.2 1z" fill="#fff"/><path d="M14 3a7 7 0 0 1 7 7M14 6.5a3.5 3.5 0 0 1 3.5 3.5" fill="none" stroke="#fff" stroke-width="1.8" stroke-linecap="round"/></svg>
    </a>
  </nav>

  <section class="info-panel">
    <h1 class="info-panel__title">Brookfen 14<br>Industrial Park</h1>
    <p class="info-panel__text">The property is located on the west side of the Town of Wrenford, a Growing Municipality Located Northeast of Harlow City, with a Regional Population of 13,649. The area has a very Strong Local economy due to its location between Harlow City and Pike Lake, but with a stronger agricultural base. It serves as the focal point for the Misty Lake area, with an Unemployment rate of 5.0% lower than the Provincial Average of 8.2%.</p>
    <div class="stats">
      <div class="stat"><div class="stat__value">13,649</div><div class="stat__label">Regional Population</div></div>
      <div class="stat"><div class="stat__value">5.0%</div><div class="stat__label">Unemployment Rate</div></div>
      <div class="stat"><div class="stat__value">8.2%</div><div class="stat__label">Provincial Average</div></div>
    </div>
    <a class="btn-learn">LEARN MORE</a>
  </section>
</div>
</body>
</html>
```